Kestrel Photography Business Card

I need a business card designed for a photography business based in Perth, Western Australia called Kestrel Photography.

We specialise in wedding, event photography and portrait photography.

The business card must borrow the style of the attached logo.

The hex codes for the colours in the logo are:
#ED1D85 - Pink
#89C23E - Green
#37282F - Black

The name on the card will be:
Name: Toviran
Phone: 0417395268
Website: www.kestrelphotography.com.au
Facebook: kestrelphotography

I am open and happy to accept creative concepts.

I’d like some space at the back for writing notes and appointment details.

```html
<!DOCTYPE html>
<html lang="en">
<head>
<meta charset="utf-8">
<title>Kestrel Photography Business Card</title>
<link rel="stylesheet" href="https://fonts.googleapis.com/css2?family=Questrial&family=Montserrat:wght@700&display=swap">
<style>
  :root {
    --stage: #e7e4e5;
    --card-dark: #45363d;
    --card-dark-soft: #52424a;
    --card-green: #a4c83f;
    --ink: #37282f;
    --pink: #ed1d85;
    --white: #ffffff;
    --text-light: #e9e2e5;
  }
  * { box-sizing: border-box; margin: 0; padding: 0; }
  html, body {
    width: 1200px;
    height: 900px;
    overflow: hidden;
    background: var(--stage);
    font-family: "Questrial", "Helvetica Neue", Arial, sans-serif;
  }
  .stage {
    position: relative;
    width: 1200px;
    height: 900px;
  }
  .card {
    position: absolute;
    left: 300px;
    width: 600px;
    height: 366px;
    border-radius: 22px;
    box-shadow: 0 10px 28px rgba(55, 40, 47, 0.22);
    overflow: hidden;
  }
  /* Back of card */
  .card-back {
    top: 70px;
    background: var(--card-dark);
  }
  .back-emblem {
    position: absolute;
    left: 50%;
    top: 50%;
    width: 230px;
    height: 230px;
    margin: -115px 0 0 -115px;
    border-radius: 50%;
    background: var(--card-dark-soft);
  }
  .back-mark {
    position: absolute;
    left: 50%;
    top: 50%;
    width: 64px;
    height: 64px;
    margin: -82px 0 0 -32px;
    border-radius: 50%;
    background: var(--pink);
  }
  .back-name {
    position: absolute;
    left: 0;
    right: 0;
    top: 215px;
    text-align: center;
    color: var(--text-light);
    font-size: 17px;
    letter-spacing: 0.45em;
    text-transform: uppercase;
    padding-left: 0.45em;
  }
  /* Front of card */
  .card-front {
    top: 464px;
    background: var(--card-green);
    color: var(--ink);
  }
  .front-mark {
    position: absolute;
    left: 50%;
    top: 28px;
    width: 78px;
    height: 78px;
    margin-left: -39px;
    border-radius: 50%;
    background: var(--pink);
  }
  .front-name {
    position: absolute;
    left: 0;
    right: 0;
    top: 124px;
    text-align: center;
    font-size: 15px;
    letter-spacing: 0.5em;
    padding-left: 0.5em;
    text-transform: uppercase;
  }
  .contact-list {
    position: absolute;
    left: 118px;
    top: 172px;
    list-style: none;
  }
  .contact-item {
    display: flex;
    align-items: center;
    height: 30px;
    font-size: 17px;
    letter-spacing: 0.2em;
    text-transform: uppercase;
  }
  .contact-icon {
    width: 16px;
    height: 16px;
    margin-right: 10px;
    flex: none;
  }
  .contact-phone { padding-left: 120px; }
  .person-name {
    position: absolute;
    left: 0;
    right: 0;
    top: 292px;
    text-align: center;
    font-family: "Montserrat", Arial, sans-serif;
    font-weight: 700;
    font-size: 15px;
    letter-spacing: 0.3em;
    padding-left: 0.3em;
    text-transform: uppercase;
  }
</style>
</head>
<body>
<main class="stage">
  <section class="card card-back">
    <div class="back-emblem"></div>
    <div class="back-mark"></div>
    <p class="back-name">Kestrel Photography</p>
  </section>

  <section class="card card-front">
    <div class="front-mark"></div>
    <h1 class="front-name">Kestrel Photography</h1>
    <ul class="contact-list">
      <li class="contact-item contact-phone">
        <svg class="contact-icon" viewBox="0 0 16 16" aria-hidden="true">
          <rect width="16" height="16" rx="2" fill="var(--white)"/>
          <path d="M5 3.5 L7 3.5 L7.6 6 L6.4 7 Q7.4 9 9 9.8 L10 8.6 L12.5 9.2 L12.5 11.2 Q12.5 12.5 11 12.5 Q4 11.8 3.5 5 Q3.5 3.5 5 3.5 Z" fill="var(--card-green)"/>
        </svg>
        <span>0417395268</span>
      </li>
      <li class="contact-item">
        <svg class="contact-icon" viewBox="0 0 16 16" aria-hidden="true">
          <rect width="16" height="16" rx="2" fill="var(--white)"/>
        </svg>
        <span>www.kestrelphotography.com.au</span>
      </li>
      <li class="contact-item">
        <svg class="contact-icon" viewBox="0 0 16 16" aria-hidden="true">
          <rect width="16" height="16" rx="2" fill="var(--white)"/>
        </svg>
        <span>kestrelphotography</span>
      </li>
    </ul>
    <p class="person-name">Toviran</p>
  </section>
</main>
</body>
</html>
```